Boutique Shoe Bag Race wear Business Card Design

We are a new luxury shoe bag, jewellery and race wear store stocking local and international designers. Located in the fashion precinct of beautiful Bondi Beach famous in Sydney Australia. Stocking French jewellery and shoes such as Maximilien verdacs plus Australian made. Looking at quality and service and looking after the locals and tourists.
Ideas: White background, Black writing in bold engravers, logo in middle of Bondi and Boutique a gold horseshoe (facing upright so the curve is at the bottom) with a black stiletto inside. French clover silver and black border (not irish clover the French lattice type look)

Larkspur Parlour

I open 8/4 so require business card design ASAP.

Please place gold horseshoe facing upwards with the black stiletto inside.

Bold engravers writing for business name.

I will have my phone number tomorrow to update.

Border in similar/same style as attached picture with black/silver clover French design.

Thank you. Petra                                   

Industry/Entity Type

Fashion

Contact Information for Business Card

Larkspur Parlour
Boutique Owner Petra Halvorsen
41B Tindle Road
Bondi Beach NSW 2026 Australia
0491237406
02 **** *TBA
info@larkspurparlour.com.au
Facebook.com/LarkspurParlour
www.larkspurparlour.com.au

Font styles to use
Other font styles liked:
• Bold Engravers

Requirements
Must have
• Info on one side including business name and logo with black stiletto and gold horse shoe. reverse side with French clover border and Larger name Larkspur Parlour with logo in centre.
Should not have
• irish clover
French script
horseshoe upside down

```html
<!DOCTYPE html>
<html lang="en">
<head>
<meta charset="utf-8">
<title>Larkspur Parlour – Business Cards</title>
<link rel="stylesheet" href="https://fonts.googleapis.com/css2?family=Pinyon+Script&family=Questrial&family=Montserrat:wght@700&display=swap">
<style>
  :root {
    --backdrop: #e9e6e2;
    --card-edge: #1c1c1c;
    --paper: #ffffff;
    --ink: #1a1a1a;
    --gold: #b8892f;
    --silver-light: #d9d9d9;
    --silver-dark: #6e6e6e;
  }
  * { box-sizing: border-box; margin: 0; padding: 0; }
  html, body { width: 1200px; height: 1000px; overflow: hidden; }
  body {
    background: var(--backdrop);
    font-family: "Questrial", "Century Gothic", sans-serif;
    color: var(--ink);
    position: relative;
  }
  .card {
    position: absolute;
    left: 200px;
    width: 800px;
    height: 440px;
    background: var(--card-edge);
    padding: 14px;
  }
  .card--front { top: 40px; }
  .card--back { top: 520px; }
  .card__face {
    position: relative;
    width: 100%;
    height: 100%;
    background: var(--paper);
  }

  /* Front */
  .clover-border {
    position: absolute;
    inset: 0;
    border: 44px solid transparent;
    border-image: linear-gradient(135deg, var(--silver-dark), var(--silver-light), var(--silver-dark)) 1;
  }
  .front__brand {
    position: absolute;
    top: 150px;
    left: 0;
    right: 0;
    display: flex;
    justify-content: center;
    align-items: center;
    gap: 24px;
    font-family: "Pinyon Script", cursive;
    font-size: 92px;
    line-height: 1;
  }
  .brand-mark {
    width: 70px;
    height: 70px;
    border-radius: 50%;
    background: var(--gold);
    flex: none;
  }
  .front__url {
    position: absolute;
    bottom: 62px;
    left: 0;
    right: 0;
    text-align: center;
    font-size: 24px;
  }

  /* Back */
  .back__brand {
    position: absolute;
    top: 22px;
    left: 46px;
    font-family: "Pinyon Script", cursive;
    font-size: 64px;
    line-height: 1;
  }
  .back__mark {
    position: absolute;
    top: 40px;
    right: 46px;
    width: 86px;
    height: 86px;
    border-radius: 50%;
    background: var(--gold);
  }
  .owner {
    position: absolute;
    top: 130px;
    left: 46px;
  }
  .owner__name {
    font-family: "Montserrat", sans-serif;
    font-weight: 700;
    font-size: 32px;
  }
  .owner__role { font-size: 34px; margin-top: 4px; }
  .contact {
    position: absolute;
    top: 278px;
    left: 46px;
    list-style: none;
    font-size: 23px;
    line-height: 32px;
  }
  .contact__item { display: flex; align-items: center; gap: 8px; }
  .contact__icon { width: 20px; height: 20px; flex: none; }
  .social-dot {
    width: 20px; height: 20px; border-radius: 50%;
    background: var(--silver-dark); flex: none;
  }
  .address {
    position: absolute;
    right: 46px;
    bottom: 34px;
    text-align: right;
    font-size: 23px;
    line-height: 30px;
  }
  .address__label { font-family: "Montserrat", sans-serif; font-weight: 700; font-size: 21px; }
</style>
</head>
<body>
  <section class="card card--front">
    <div class="card__face">
      <div class="clover-border" role="img" aria-label="Border of alternating black and silver lattice clovers"></div>
      <h1 class="front__brand">
        <span>Larkspur</span><span class="brand-mark"></span><span>Parlour</span>
      </h1>
      <p class="front__url">www.larkspurparlour.com.au</p>
    </div>
  </section>

  <section class="card card--back">
    <div class="card__face">
      <h2 class="back__brand">Larkspur Parlour</h2>
      <span class="back__mark"></span>
      <div class="owner">
        <p class="owner__name">Petra Halvorsen</p>
        <p class="owner__role">Boutique Owner</p>
      </div>
      <ul class="contact">
        <li class="contact__item">
          <svg class="contact__icon" viewBox="0 0 20 20"><rect x="6" y="1" width="8" height="18" rx="1.5" fill="none" stroke="#6e6e6e" stroke-width="1.5"/><line x1="9" y1="16" x2="11" y2="16" stroke="#6e6e6e" stroke-width="1.5"/></svg>
          0491237406 02
        </li>
        <li class="contact__item">
          <svg class="contact__icon" viewBox="0 0 20 20"><rect x="1" y="4" width="18" height="12" fill="none" stroke="#6e6e6e" stroke-width="1.5"/><polyline points="1,4 10,11 19,4" fill="none" stroke="#6e6e6e" stroke-width="1.5"/></svg>
          info@larkspurparlour.com.au
        </li>
        <li class="contact__item">
          <span class="social-dot"></span>
          Facebook.com/LarkspurParlour
        </li>
      </ul>
      <address class="address" style="font-style:normal">
        <p class="address__label">Address</p>
        <p>41B Tindle Road</p>
        <p>Bondi Beach</p>
        <p>NSW 2026 Australia</p>
      </address>
    </div>
  </section>
</body>
</html>
```